New Business Card for Auto Repair and Performance Shop!

Need a redesign on a card that we have used for a while now. Something more update and modern, Serious but not too serious. Something confident, that shows the client that we are bespoke. Adding value.

Target Market(s)

Foreign Auto Repair and Performance

Industry/Entity Type

Automotive

Contact Information for Business Card

Utilize Logo, would like to change car silhouette to something Veltra,

Font styles to use
Sans Serif

Requirements
Must have
• business name, address, website, phone number.
MotoSerenix
4918 W. Birchwell Rd
Marrowvale, Q.X. 00417
1-254-487-3106
www.moto-serenix-example.com

Specializing in Asian, European, and Domestic Auto Repair, Performance and Fabrication.

Clear space on back to for space to write appointment time and which client advisor helped the client.
Nice to have
• Up to the designers,

```html
<!DOCTYPE html>
<html lang="en">
<head>
<meta charset="utf-8">
<title>MotoSerenix Business Cards</title>
<link rel="stylesheet" href="https://fonts.googleapis.com/css2?family=Lato:wght@300;400;700&family=Poppins:wght@300;600&display=swap">
<style>
  :root {
    --ink: #1b1b1d;
    --card-black: #0e0f11;
    --paper: #ffffff;
    --accent: #e0312b;
    --muted: #8a8a8a;
    --line: #333333;
    --backdrop: #e9e7e3;
  }
  html, body {
    margin: 0;
    padding: 0;
    width: 1200px;
    height: 1200px;
    overflow: hidden;
    background: var(--backdrop);
  }
  .canvas {
    position: relative;
    width: 1200px;
    height: 1200px;
    font-family: "Lato", sans-serif;
    color: var(--ink);
  }
  .card {
    position: absolute;
    left: 170px;
    width: 860px;
    height: 491px;
    background: var(--paper);
    overflow: hidden;
    box-shadow: 0 6px 22px rgba(0,0,0,0.18);
  }
  .card--back { top: 80px; }
  .card--front { top: 630px; }

  /* Back */
  .back-band {
    position: absolute;
    inset: 0;
    width: 860px;
    height: 491px;
  }
  .back-band polygon { fill: var(--card-black); }
  .back-brand {
    position: absolute;
    left: 330px;
    top: 100px;
    width: 470px;
    font-weight: 700;
    font-size: 30px;
    letter-spacing: 4px;
    color: var(--paper);
    display: flex;
    justify-content: flex-end;
    align-items: center;
    gap: 14px;
  }
  .brand-dot {
    width: 16px;
    height: 16px;
    border-radius: 50%;
    background: var(--accent);
  }
  .tagline {
    position: absolute;
    left: 250px;
    top: 170px;
    width: 560px;
    margin: 0;
    color: var(--paper);
    font-size: 17px;
    line-height: 1.45;
    letter-spacing: 3px;
    text-transform: uppercase;
    text-align: right;
  }
  .appointment-label {
    position: absolute;
    left: 70px;
    top: 360px;
    font-size: 17px;
    letter-spacing: 4px;
    text-transform: uppercase;
    color: var(--ink);
  }
  .appointment-line {
    position: absolute;
    left: 70px;
    top: 425px;
    width: 720px;
    height: 0;
    border-top: 1.5px solid var(--line);
  }

  /* Front */
  .person-name {
    position: absolute;
    left: 80px;
    top: 62px;
    margin: 0;
    font-family: "Poppins", sans-serif;
    font-weight: 600;
    font-size: 36px;
    color: var(--ink);
  }
  .person-title {
    position: absolute;
    left: 80px;
    top: 110px;
    margin: 0;
    font-family: "Poppins", sans-serif;
    font-weight: 300;
    font-size: 20px;
    color: var(--muted);
  }
  .contact-list {
    position: absolute;
    left: 80px;
    top: 215px;
    margin: 0;
    padding: 0;
    list-style: none;
    font-size: 22px;
    color: var(--ink);
  }
  .contact-list li {
    display: flex;
    align-items: center;
    gap: 16px;
    height: 40px;
  }
  .icon { width: 22px; height: 22px; flex: none; }
  .icon path, .icon rect, .icon circle, .icon line { stroke: var(--accent); fill: none; stroke-width: 2; }
  .icon .solid { fill: var(--accent); stroke: none; }
  .icon .pin-hole { fill: var(--paper); stroke: none; }
  .front-brand {
    position: absolute;
    left: 470px;
    top: 200px;
    display: flex;
    align-items: center;
    gap: 14px;
    font-weight: 700;
    font-size: 36px;
    letter-spacing: 3px;
    color: var(--ink);
  }
  .front-brand .brand-dot { width: 18px; height: 18px; }
  .address {
    position: absolute;
    left: 470px;
    top: 320px;
    display: flex;
    gap: 18px;
    align-items: flex-start;
  }
  .address .icon { width: 24px; height: 30px; margin-top: 4px; }
  .address-text {
    font-style: normal;
    font-size: 24px;
    line-height: 1.3;
    color: var(--ink);
  }
  .address-name {
    display: block;
    font-weight: 700;
    font-size: 26px;
  }
</style>
</head>
<body>
<main class="canvas">

  <section class="card card--back" aria-label="Card back">
    <svg class="back-band" viewBox="0 0 860 491" aria-hidden="true">
      <polygon points="0,0 860,0 860,380 0,280"/>
    </svg>
    <div class="back-brand"><span class="brand-dot"></span>MOTOSERENIX</div>
    <p class="tagline">Specializing in Asian, European, and Domestic<br>Auto Repair, Performance and Fabrication.</p>
    <div class="appointment-label">Appointment Time</div>
    <div class="appointment-line"></div>
  </section>

  <section class="card card--front" aria-label="Card front">
    <h1 class="person-name">Person Name</h1>
    <p class="person-title">CEO</p>

    <ul class="contact-list">
      <li>
        <svg class="icon" viewBox="0 0 22 22" aria-hidden="true">
          <rect x="6" y="1.5" width="10" height="19" rx="2"/>
          <line x1="9" y1="17" x2="13" y2="17"/>
        </svg>
        1-254-487-3106
      </li>
      <li>
        <svg class="icon" viewBox="0 0 22 22" aria-hidden="true">
          <circle cx="11" cy="11" r="9"/>
          <line x1="2" y1="11" x2="20" y2="11"/>
          <path d="M11 2 C6 7 6 15 11 20 M11 2 C16 7 16 15 11 20"/>
        </svg>
        www.moto-serenix-example.com
      </li>
    </ul>

    <div class="front-brand"><span class="brand-dot"></span>MOTOSERENIX</div>

    <div class="address">
      <svg class="icon" viewBox="0 0 24 30" aria-hidden="true">
        <path class="solid" d="M12 0 C5.4 0 1 4.8 1 11 C1 19 12 30 12 30 C12 30 23 19 23 11 C23 4.8 18.6 0 12 0 Z"/>
        <circle class="pin-hole" cx="12" cy="11" r="4"/>
      </svg>
      <address class="address-text">
        <span class="address-name">MotoSerenix</span>
        4918 W. Birchwell Rd<br>
        Marrowvale, Q.X. 00417
      </address>
    </div>
  </section>

</main>
</body>
</html>
```